one page website design - crestloomworks.net

hello.
need a design for crestloomworks.net - small community of developers that create web sites, services and products in cooperation with entrepreneurs for free.
The main condition is that the venture should be a startup. Community has the right to reject the project if they dislike it. Their motivation is to help developing new great services and get share in business. It's a kind of angel investment on seed stage made by developers :)

It should be 1 page scrollable (paralax) website
You can find sections and the text at rough mockup attached. You can pick any colors and style, up to you. Images at mockup should be substituted with other ones (you have the right to use) or with icons. But they have to fit the idea of each section well. The position of the text the way it's placed can be also changed.
Basically anything can be implemented not like in mockup :) It was done just to explain the idea.

Please include simple minimalistic logo.
Design has to be responsive and look well from tablets and smartphones.
Please display how errors have to look line at the form in the bottom. Also result of form submission

Result has to in PSD with versions for tablet and smartphone + logo in separate file in PNG with transparent background.

Target Market(s)

startups, community, venture funding, programming, angel investments

Industry/Entity Type

Community

Number of Pages Required

1 page

Requirements
Must have
• Design has to be responsive and look well from tablets and smartphones.
• Result has to in PSD with versions for tablet and smartphone + logo in separate file in PNG with transparent background.
Should not have
• images that used by many other websites on the web

```html
<!DOCTYPE html>
<html lang="en">
<head>
<meta charset="utf-8">
<title>Crestloom Works — one page</title>
<link href="https://fonts.googleapis.com/css2?family=Open+Sans:wght@400;600;700&family=Playfair+Display:wght@700;900&display=swap" rel="stylesheet">
<style>
:root{
  --green:#8cc63f;
  --green-dark:#6fa62a;
  --blue:#1e88e5;
  --navy:#14324f;
  --ink:#222;
  --muted:#777;
  --paper:#f3f3f1;
  --slate:#34495e;
  --teal:#1aaf9b;
  --purple:#7b3fa0;
  --red:#e4543f;
  --white:#fff;
}
*{box-sizing:border-box;margin:0;padding:0}
html,body{width:1200px;height:2540px;overflow:hidden}
body{font-family:"Open Sans",Arial,sans-serif;color:var(--ink);background:var(--white);position:relative}
.serif{font-family:"Playfair Display",Georgia,serif}

/* hero */
.hero{position:absolute;left:0;top:0;width:1200px;height:600px}
.hero-photo{position:absolute;inset:0;background:linear-gradient(135deg,#5b6a6e 0%,#3b4548 45%,#2a2f31 100%)}
.hero-shade{position:absolute;inset:0;background:linear-gradient(90deg,rgba(0,0,0,.05),rgba(0,0,0,.45))}
.logo{position:absolute;left:150px;top:14px;display:flex;align-items:center;gap:12px}
.logo-dot{width:72px;height:72px;border-radius:50%;background:var(--green)}
.logo-name{font-weight:700;font-size:22px;color:var(--white)}
.nav{position:absolute;right:150px;top:62px;display:flex;align-items:center;gap:48px;font-size:15px;color:var(--white)}
.nav .apply{background:var(--blue);padding:6px 38px;border-radius:3px;font-weight:600}
.hero-copy{position:absolute;left:612px;top:295px;width:420px;color:var(--white);font-size:22px;line-height:1.3}
.hero-copy .accent{font-family:"Playfair Display",Georgia,serif;font-weight:900;font-size:30px;color:var(--white);letter-spacing:1px}
.hero-copy .tag{margin-top:34px;font-size:16px;color:var(--green);font-weight:600}
.hero-arrows{position:absolute;left:232px;top:488px;display:flex;gap:14px}
.hero-arrows span{width:32px;height:32px;border-radius:50%;display:flex;align-items:center;justify-content:center}
.hero-arrows .prev{background:var(--blue)}
.hero-arrows .next{background:var(--green)}

/* how it works */
.how{position:absolute;left:0;top:600px;width:1200px;height:905px;background:var(--paper)}
.how-title{position:absolute;left:232px;top:82px;font-size:30px;line-height:1.15;font-weight:900}
.step{position:absolute;width:360px}
.step-num{position:absolute;top:-52px;right:10px;font-family:"Playfair Display",Georgia,serif;font-size:64px;font-weight:900;color:#e2e2df}
.step-art{position:relative;height:200px}
.step-label{position:absolute;left:0;bottom:0;background:rgba(0,0,0,.55);color:var(--white);font-size:17px;padding:5px 14px;font-weight:600}
.step-label b{color:var(--green);font-family:"Playfair Display",Georgia,serif}
.step-note{font-size:12px;color:var(--muted);margin-top:6px;line-height:1.45;padding-left:4px}
.s1{left:612px;top:80px}.s1 .step-art{background:var(--slate)}
.s2{left:232px;top:240px}.s2 .step-art{background:var(--teal)}
.s3{left:612px;top:410px}.s3 .step-art{background:var(--purple)}
.s4{left:232px;top:580px}.s4 .step-art{background:var(--red)}

/* terms */
.terms{position:absolute;left:0;top:1505px;width:1200px;height:325px;background:var(--white)}
.terms-band{position:absolute;left:155px;top:0;width:890px;height:325px;background:linear-gradient(135deg,#1d4c78 0%,var(--navy) 70%,#0f253b 100%);color:var(--white)}
.terms-title{position:absolute;left:78px;top:50px;font-size:30px;font-weight:900}
.terms-col{position:absolute;top:118px;font-size:14px}
.terms-col h3{font-size:17px;font-weight:400;margin-bottom:10px}
.terms-col h3 em{font-style:normal;color:var(--green);font-weight:700}
.terms-col li{list-style:none;display:flex;align-items:center;gap:10px;margin-bottom:5px;color:#dce6ef}
.terms-col li::before{content:"";width:10px;height:10px;background:var(--white);opacity:.8;flex:none}
.col-left{left:78px}.col-right{left:530px}

/* contact */
.talk{position:absolute;left:0;top:1880px;width:1200px;text-align:center}
.talk h2{font-size:30px;font-weight:900}
.talk p{font-size:12px;color:var(--muted);margin-top:8px}
.keys{position:absolute;left:0;top:1980px;width:1200px;height:220px;background:linear-gradient(180deg,#3a3a3a,#1c1c1c)}
.green-band{position:absolute;left:0;top:2200px;width:1200px;height:340px;background:var(--green)}
.form{position:absolute;left:290px;top:2080px;width:620px;height:265px;background:var(--white);box-shadow:0 4px 16px rgba(0,0,0,.15)}
.field{position:absolute;left:20px;width:280px;height:34px;border:1px solid #ddd;border-radius:3px;font-size:12px;color:#999;padding:9px 12px}
.f1{top:48px}.f2{top:92px}.f3{top:136px;width:180px}
.attach{position:absolute;left:205px;top:136px;width:95px;height:34px;background:#eee;border:1px solid #ddd;border-radius:3px;font-size:12px;color:#666;display:flex;align-items:center;justify-content:center}
.textarea{position:absolute;left:318px;top:48px;width:282px;height:122px;border:1px solid #ddd;border-radius:3px;font-size:12px;color:#999;padding:9px 12px}
.submit{position:absolute;left:250px;top:196px;width:120px;height:34px;border-radius:17px;background:var(--green);color:var(--white);font-size:13px;font-weight:600;display:flex;align-items:center;justify-content:center}

/* footer */
.footer-logo{position:absolute;left:155px;top:2400px;display:flex;align-items:center;gap:12px}
.footer-logo .logo-dot{background:#1b1b1b}
.footer-logo .logo-name{color:#1b1b1b}
.copy{position:absolute;left:0;top:2442px;width:1200px;text-align:center;font-size:12px;color:#2c3a12}
.social{position:absolute;left:860px;top:2432px;display:flex;gap:10px}
.social span{width:26px;height:26px;border-radius:50%;background:#2c3a12}
.to-top{position:absolute;left:1016px;top:2432px;width:28px;height:28px;border-radius:50%;background:#1b1b1b;display:flex;align-items:center;justify-content:center}
</style>
</head>
<body>

<header class="hero">
  <div class="hero-photo" role="img" aria-label="Photo of a team of developers working together around a table"></div>
  <div class="hero-shade"></div>
  <div class="logo"><span class="logo-dot"></span><span class="logo-name">Crestloom Works</span></div>
  <nav class="nav">
    <span>How It Works</span>
    <span>Terms and Projects</span>
    <span>Room</span>
    <span class="apply">Apply</span>
  </nav>
  <div class="hero-copy">
    We are a community of<br>
    <span class="accent">web developers</span> that enjoy<br>
    creating innovative products<br>and services
    <div class="tag">Since 2016</div>
  </div>
  <div class="hero-arrows">
    <span class="prev"><svg width="12" height="12" viewBox="0 0 12 12"><path d="M8 2 4 6l4 4" stroke="#fff" stroke-width="2" fill="none"/></svg></span>
    <span class="next"><svg width="12" height="12" viewBox="0 0 12 12"><path d="M4 2l4 4-4 4" stroke="#fff" stroke-width="2" fill="none"/></svg></span>
  </div>
</header>

<section class="how">
  <h2 class="how-title serif">How<br>It Works</h2>

  <div class="step s1">
    <span class="step-num">01</span>
    <div class="step-art" role="img" aria-label="Illustration of gears and a light bulb for an idea">
      <div class="step-label">You Submit <b>Idea / Plan</b></div>
    </div>
    <p class="step-note">with extended marketing plan (if you have already)</p>
  </div>

  <div class="step s2">
    <span class="step-num">02</span>
    <div class="step-art" role="img" aria-label="Illustration of a support person with a headset">
      <div class="step-label">Schedule <b>Callnest Call</b></div>
    </div>
    <p class="step-note">and discuss it with you</p>
  </div>

  <div class="step s3">
    <span class="step-num">03</span>
    <div class="step-art" role="img" aria-label="Illustration of a team meeting around a table">
      <div class="step-label">Make <b>Decision</b></div>
    </div>
    <p class="step-note">after discuss internally</p>
  </div>

  <div class="step s4">
    <span class="step-num">04</span>
    <div class="step-art" role="img" aria-label="Illustration of a rocket launching">
      <div class="step-label">Start the <b>Project</b></div>
    </div>
    <p class="step-note">if our decision is positive we proceed with<br>marketing plan</p>
  </div>
</section>

<section class="terms">
  <div class="terms-band" role="img" aria-label="Dark blue photo backdrop of a workspace">
    <h2 class="terms-title serif">Terms &amp; Projects</h2>
    <div class="terms-col col-left">
      <h3><em>Agreement</em> we sign. <em>Sponsors</em> that:</h3>
      <ul>
        <li>We get 40% share in venture</li>
        <li>Project is hosted on our servers</li>
        <li>Domain belongs to our account</li>
        <li>We are responsible for development</li>
        <li>You are responsible for marketing goals</li>
      </ul>
    </div>
    <div class="terms-col col-right">
      <h3>Projects <em>We Evolve:</em></h3>
      <ul>
        <li>Early proof of concept</li>
        <li>Revenue generation supposed after release</li>
        <li>B2C service or product</li>
        <li>Advertising based business model</li>
      </ul>
    </div>
  </div>
</section>

<section class="talk">
  <h2 class="serif">Lets Talk</h2>
  <p>Tell the details your project below or just say hello.</p>
</section>

<div class="keys" role="img" aria-label="Close-up photo of a dark keyboard"></div>
<div class="green-band"></div>

<form class="form">
  <div class="field f1">Your Name</div>
  <div class="field f2">Enter your Email</div>
  <div class="field f3">Startup Site</div>
  <div class="attach">Attach</div>
  <div class="textarea">Idea Description...</div>
  <div class="submit">Submit</div>
</form>

<footer>
  <div class="footer-logo"><span class="logo-dot"></span><span class="logo-name">Crestloom Works</span></div>
  <p class="copy">© Crestloom Works 2016</p>
  <div class="social"><span></span><span></span><span></span><span></span></div>
  <span class="to-top"><svg width="12" height="12" viewBox="0 0 12 12"><path d="M2 8l4-4 4 4" stroke="#fff" stroke-width="2" fill="none"/></svg></span>
</footer>

</body>
</html>
```